New Webpage for High Class Expert Witness Services Company

We are looking for a minimalist design for a webpage that just has our logo and an entry form offer to connect with one of our Liaisons.
The entry form should just ask for Name, Email, Contact Info and Description of Project.

Company Name is: The Marlow Crest Advisory Services

Number of Pages Required

1 page

```html
<!DOCTYPE html>
<html lang="en">
<head>
<meta charset="utf-8">
<title>The Marlow Crest Advisory Services</title>
<link href="https://fonts.googleapis.com/css2?family=Manrope:wght@300;400;500;600;700;800&family=Inter:wght@400;500;600&display=swap" rel="stylesheet">
<style>
:root{
  --bg:#111111;
  --bg-form:#141414;
  --field:#1f2020;
  --text:#ffffff;
  --muted:#bdbdbd;
  --dim:#8a8a8a;
  --faint:#4a4a4a;
  --button:#c4c4c4;
  --button-text:#2e2e2e;
  --line:#1d1d1d;
}
*{margin:0;padding:0;box-sizing:border-box}
html,body{width:1200px;height:2301px;overflow:hidden;background:var(--bg);color:var(--text);font-family:"Manrope",sans-serif}
.site-header{position:absolute;top:0;left:0;width:1200px;height:94px}
.brand{position:absolute;left:30px;top:22px;width:150px;height:49px;background:#161616;display:flex;align-items:center;gap:7px;padding:0 10px}
.brand-mark{width:12px;height:12px;background:#d8d8d8;flex:none}
.brand-name{font-size:9px;font-weight:600;line-height:1.15;color:#d8d8d8;letter-spacing:.02em}
.main-nav{position:absolute;top:36px;left:394px;display:flex;gap:37px;font-size:15px;font-weight:300;color:var(--muted)}
.portal-btn{position:absolute;left:1013px;top:30px;width:157px;height:34px;background:var(--button);color:var(--button-text);font-family:"Inter",sans-serif;font-weight:600;font-size:13px;letter-spacing:.06em;display:flex;align-items:center;justify-content:center}
.hero{position:absolute;top:94px;left:0;width:1200px;height:836px}
.hero-visual{position:absolute;left:722px;top:26px;width:478px;height:810px;background:linear-gradient(90deg,rgba(20,20,20,0) 0%,#151515 60%,#161616 100%)}
.hero-title{position:absolute;left:30px;top:176px;font-size:90px;font-weight:800;line-height:90px;letter-spacing:-.035em}
.hero-lead{position:absolute;left:30px;top:568px;width:540px;font-size:23.5px;font-weight:300;line-height:30px;color:var(--muted)}
.contact{position:absolute;top:930px;left:0;width:1200px;height:866px;background:var(--bg-form)}
.eyebrow{position:absolute;top:120px;width:1200px;text-align:center;font-family:"Inter",sans-serif;font-size:12px;letter-spacing:.32em;color:var(--muted)}
.contact-title{position:absolute;top:146px;width:1200px;text-align:center;font-size:45px;font-weight:600;letter-spacing:-.02em}
.field{position:absolute}
.field label{display:block;font-family:"Inter",sans-serif;font-size:10px;letter-spacing:.12em;color:var(--muted);margin-bottom:9px}
.field .input{height:52px;background:var(--field);padding:0 22px;display:flex;align-items:center;font-size:15px;font-weight:300;color:#5a5b5b;text-transform:uppercase}
.field .textarea{height:142px;align-items:flex-start;padding-top:18px}
.submit-btn{position:absolute;left:436px;top:680px;width:328px;height:52px;background:var(--button);color:var(--button-text);font-family:"Inter",sans-serif;font-size:12px;font-weight:600;letter-spacing:.2em;display:flex;align-items:center;justify-content:center}
.feature{position:absolute;top:1796px;left:0;width:1200px;height:360px;background:linear-gradient(90deg,#0d0d0d,#111 50%,#0d0d0d)}
.feature-image{position:absolute;left:286px;top:0;width:652px;height:360px;background:radial-gradient(ellipse at 48% 55%,#2a2a2a 0%,#151515 55%,#0c0c0c 100%)}
.site-footer{position:absolute;top:2156px;left:0;width:1200px;height:145px;background:var(--bg);border-top:1px solid var(--line)}
.footer-brand{position:absolute;left:45px;top:46px;font-size:18px;font-weight:600;line-height:27px;width:150px}
.footer-link{position:absolute;top:65px;font-family:"Inter",sans-serif;font-size:12px;letter-spacing:.14em;line-height:15px;color:var(--faint)}
.copyright{position:absolute;right:45px;top:65px;width:360px;text-align:right;font-family:"Inter",sans-serif;font-size:10px;letter-spacing:.12em;line-height:14px;color:#3a3a3a;text-transform:uppercase}
</style>
</head>
<body>
<header class="site-header">
  <div class="brand"><span class="brand-mark"></span><span class="brand-name">The Marlow Crest Advisory Services</span></div>
  <nav class="main-nav"><span>Operations</span><span>Technology</span><span>Personnel</span><span>Intelligence</span></nav>
  <div class="portal-btn">SECURE PORTAL</div>
</header>

<section class="hero">
  <div class="hero-visual" role="img" aria-label="Dark atmospheric backdrop"></div>
  <h1 class="hero-title">Seamless<br>Medical<br>Expert<br>Integration</h1>
  <p class="hero-lead">Precision-engineered security intelligence met with elite medical counsel. Connect with a dedicated Liaison to orchestrate specialized tactical medical expertise for critical operations.</p>
</section>

<section class="contact">
  <div class="eyebrow">ENGAGEMENT PROTOCOL</div>
  <h2 class="contact-title">Initiate Liaison Contact</h2>
  <div class="field" style="left:240px;top:262px;width:345px"><label>FULL NAME</label><div class="input">Operative Identity</div></div>
  <div class="field" style="left:615px;top:262px;width:345px"><label>SECURE EMAIL</label><div class="input">Encrypted Address</div></div>
  <div class="field" style="left:240px;top:366px;width:720px"><label>CONTACT INFORMATION</label><div class="input">Secure Channel</div></div>
  <div class="field" style="left:240px;top:470px;width:720px"><label>DESCRIPTION OF PROJECT</label><div class="input textarea">Mission Objectives and Scope</div></div>
  <div class="submit-btn">SUBMIT ENGAGEMENT REQUEST</div>
</section>

<section class="feature">
  <div class="feature-image" role="img" aria-label="Dark render of a secure device displaying a shield emblem"></div>
</section>

<footer class="site-footer">
  <div class="footer-brand">The Marlow Crest</div>
  <div class="footer-link" style="left:229px">PRIVACY<br>PROTOCOL</div>
  <div class="footer-link" style="left:385px">TERMS OF<br>ENGAGEMENT</div>
  <div class="footer-link" style="left:572px">ENCRYPTION<br>STANDARDS</div>
  <div class="copyright">© 2024 The Marlow Crest Advisory Services. All rights reserved.</div>
</footer>
</body>
</html>
```